Business Card Design for Vintage Jazz

I am a vintage jazz band leader in New York City. My groups play the music of the 1920s, 1930s and 1940s. My website is morvainhale.com for more info on what I do.

I am looking for a two sided business card design that has the look and feel of a really nice business card from the 1930s. I need to convey with the design that my work has that vintage kind of class and style, but also conveys that we are fun and entertaining.

Most importantly it should make a bold staement. If Walt Pemberly had a card, what would it have looked like? I want a card that I feel confident will make an impact and will let people know that my work is te the top that NYC has to offer in vintage jazz..

Note that I have only decided to avoid the "committed payment" option as I have not used this service before. Assuming that I get quality work I will select a design from those presented.

Target Market(s)

people who want to hire my band for events, media, and new fans of the band

Industry/Entity Type

Performing Art

Contact Information for Business Card

Definitely a matte finish, possibly a sort of old style of paper with that brown tint? definitely a thick card.

Requirements
Must have
• FRONT
• My name: Tobias Merrow
• What I do: Bandleader, Guitarist, Vocalist, Songwriter
• Contact Details: morvainhale.com tobias@morvainhale.com 646-555-0184
• BACK
• My Social Media Links:
• facebook.morvainhale.com
• twitter, instagram, linkedin: morvainhale
• I'm also including a photo image I would like to use. The photo's background is not needed, and to be honest isn't really desireable. Just looking to use the image of me.
Nice to have
• I'm attaching which could be used as is, omitted from the card, or altered maybe with text going around the outside of the circle or in some other way. It may need some clean up to the edges of the lettering as we only use it for the website thumbnail.
• If there's space I'd like to include the text "join our mailing list for a free song download: freesong.morvainhale.com" If not perhaps just "Download a Free Song at: freesong.morvainhale.com - something to this end.
Should not have
• anything cartoony. Don't think retro 90s's vision of the swing era, think actual swing era!
• anything modern. Got to look old school
• Try to avoid dark backgrounds. Since we often play in bars and clubs where it is dar, a d
• avoid script fonts.

```html
<!DOCTYPE html>
<html lang="en">
<head>
<meta charset="utf-8">
<title>Tobias Merrow – Business Card</title>
<link href="https://fonts.googleapis.com/css2?family=Source+Sans+3:ital,wght@0,400;0,600;1,400;1,600&display=swap" rel="stylesheet">
<style>
  :root {
    --page-bg: #2a2a2a;
    --ink: #0b0b0b;
    --paper: #ffffff;
    --text-dark: #111111;
    --text-mid: #555555;
    --text-light: #f2f2f2;
    --photo-black: #050505;
    --photo-suit: #2b2b2b;
    --photo-grey: #7a7a7a;
    --photo-light: #e6e6e6;
  }
  * { box-sizing: border-box; margin: 0; padding: 0; }
  html, body {
    width: 1200px; height: 886px; overflow: hidden;
    background: var(--page-bg);
    font-family: "Source Sans 3", "Myriad Pro", sans-serif;
  }
  .canvas { position: relative; width: 1200px; height: 886px; }
  .card {
    position: absolute; width: 566px; height: 323px;
    border-radius: 16px; overflow: hidden;
  }
  .card--front { left: 315px; top: 102px; background: var(--paper); }
  .card--back { left: 313px; top: 460px; background: var(--ink); }

  .portrait {
    position: absolute; left: 0; top: 0; width: 340px; height: 323px;
    background:
      radial-gradient(ellipse 130px 190px at 150px 220px, var(--photo-suit) 0%, rgba(43,43,43,0.85) 45%, rgba(122,122,122,0.35) 80%, rgba(255,255,255,0) 100%),
      linear-gradient(90deg, var(--photo-black) 0%, var(--photo-black) 16%, var(--photo-grey) 36%, var(--photo-light) 72%, var(--paper) 100%);
  }

  .brand-mark {
    position: absolute; display: flex; align-items: center; justify-content: center;
    border-radius: 50%; text-align: center; font-weight: 600; line-height: 1.05;
  }
  .card--front .brand-mark {
    left: 419px; top: 24px; width: 122px; height: 122px;
    background: var(--ink); color: var(--paper); font-size: 19px;
  }
  .card--back .brand-mark {
    left: 218px; top: 62px; width: 130px; height: 130px;
    background: var(--paper); color: var(--ink); font-size: 20px;
  }

  .identity {
    position: absolute; right: 24px; top: 164px; text-align: right;
  }
  .identity__name { font-size: 20px; font-weight: 600; color: var(--text-dark); line-height: 24px; }
  .identity__role { font-size: 16px; color: var(--text-mid); line-height: 20px; }

  .contact-list {
    position: absolute; right: 22px; top: 236px; list-style: none;
  }
  .contact-list li {
    display: flex; align-items: center; justify-content: flex-end;
    font-size: 15px; color: var(--text-mid); height: 21px;
  }
  .contact-list svg { width: 14px; height: 14px; margin-left: 9px; fill: var(--ink); }

  .divider {
    position: absolute; left: 31px; top: 240px; width: 505px; height: 1px;
    background: var(--text-light);
  }
  .social {
    position: absolute; left: 31px; top: 250px; list-style: none;
  }
  .social li {
    display: flex; align-items: center; height: 27px;
    font-size: 16px; color: var(--text-light);
  }
  .social__dot {
    width: 20px; height: 20px; border-radius: 50%;
    border: 2px solid var(--text-light);
    margin-right: 9px; flex: none;
  }
  .free-song {
    position: absolute; right: 30px; top: 253px; text-align: right;
    color: var(--text-light); font-style: italic; line-height: 24px;
  }
  .free-song__lead { font-size: 15px; font-weight: 400; }
  .free-song__url { font-size: 16px; font-weight: 600; }
</style>
</head>
<body>
<main class="canvas">
  <section class="card card--front" aria-label="Business card front">
    <div class="portrait" role="img" aria-label="Photo of the bandleader in a striped blazer tipping a boater hat"></div>
    <div class="brand-mark">Morvain<br>Hale</div>
    <div class="identity">
      <p class="identity__name">Tobias Merrow</p>
      <p class="identity__role">Bandleader, Guitarist</p>
      <p class="identity__role">Vocalist, Songwriter</p>
    </div>
    <ul class="contact-list">
      <li>646-555-0184
        <svg viewBox="0 0 14 14" aria-hidden="true"><path d="M3.5 0h7a1 1 0 0 1 1 1v12a1 1 0 0 1-1 1h-7a1 1 0 0 1-1-1V1a1 1 0 0 1 1-1zm.6 1.6v9.6h5.8V1.6zM7 11.8a.7.7 0 1 0 0 1.4.7.7 0 0 0 0-1.4z"/></svg>
      </li>
      <li>tobias@morvainhale.com
        <svg viewBox="0 0 14 14" aria-hidden="true"><path d="M0 3h14v8H0zm1.2 1.1v.3L7 8l5.8-3.6v-.3z"/></svg>
      </li>
      <li>morvainhale.com
        <svg viewBox="0 0 14 14" aria-hidden="true"><circle cx="7" cy="7" r="7"/><path d="M3 5c1-1 2 0 3 1s0 2 1 3-1 2-1 3M9 2c0 1 1 2 2 2s1 2 2 2" stroke="#fff" stroke-width="1.2" fill="none"/></svg>
      </li>
    </ul>
  </section>

  <section class="card card--back" aria-label="Business card back">
    <div class="brand-mark">Morvain<br>Hale</div>
    <div class="divider"></div>
    <ul class="social">
      <li><span class="social__dot"></span>morvainhale.com</li>
      <li><span class="social__dot"></span>morvainhale</li>
    </ul>
    <div class="free-song">
      <p class="free-song__lead">Download a Free Song at:</p>
      <p class="free-song__url">freesong.morvainhale.com</p>
    </div>
  </section>
</main>
</body>
</html>
```